Website Redesign project for agency

we're looking to see some new designs for an agency website.
details in this google doc: https://files.brindlepath.example/sheet/d/7QXvRk2PaLw9HsNe4TyUc8JbZoMf3Gd61572-qKrA9w/view?mode=shared
homepage and one inner page/ or the blog page
please visit the google doc above to see the website that needs to be redesigned as well as an example website we like.
if you have any questions please send them to us asap
thank you
Target Market(s)
small business owners
Number of Pages Required
2 page
Font styles to use
Sans Serif
Requirements
Nice to have
- custom design
Should not have
- do not use a template you find online

```html
<!DOCTYPE html>
<html lang="en">
<head>
<meta charset="utf-8">
<title>Rise And Reach — Web Design &amp; Inbound Marketing</title>
<link rel="stylesheet" href="https://fonts.googleapis.com/css2?family=Lato:wght@400;700&family=Montserrat:wght@500;600;800;900&display=swap">
<style>
:root{
  --coral:#e8684f;
  --peach:#fde3da;
  --ink:#2f2f2f;
  --charcoal:#3b3b3b;
  --hero-dark:#2b2b2b;
  --green:#1e7d63;
  --green-text:#1d5546;
  --card:#fdf2ec;
  --violet:#b393e0;
  --white:#ffffff;
  --muted:#4a4a4a;
}
*{box-sizing:border-box;margin:0;padding:0}
html,body{width:1200px;height:4773px;overflow:hidden}
body{position:relative;font-family:"Lato",sans-serif;color:var(--ink);background:var(--white)}
.abs{position:absolute}
.section-title{position:absolute;left:0;width:1200px;text-align:center;font-family:"Montserrat",sans-serif;font-weight:900;font-size:44px;letter-spacing:1px;color:var(--charcoal)}
.title-rule{position:absolute;left:567px;width:66px;height:3px;background:var(--coral)}
.btn{position:absolute;display:flex;align-items:center;justify-content:center;border-radius:8px;font-family:"Lato",sans-serif;font-size:22px}

/* top bar */
.top-bar{top:0;left:0;width:1200px;height:65px;background:var(--coral)}
.social-dot{position:absolute;top:16px;width:32px;height:32px;border-radius:50%;border:3px solid var(--white)}

/* hero */
.hero{top:65px;left:0;width:1200px;height:666px;background:radial-gradient(ellipse at 62% 35%,#5a5a5a 0%,#3a3a3a 40%,var(--hero-dark) 80%)}
.brand{position:absolute;font-family:"Montserrat",sans-serif;font-weight:800;font-size:36px;color:var(--white);letter-spacing:.5px}
.nav{position:absolute;top:121px;left:561px;display:flex;gap:22px;font-family:"Montserrat",sans-serif;font-weight:600;font-size:16px;color:var(--white)}
.hero-text{position:absolute;top:555px;left:176px;width:600px;font-size:30px;line-height:30px;color:var(--white)}

/* intro */
.intro-text{top:808px;left:267px;width:700px;font-size:22px;line-height:30px;font-weight:700;color:var(--charcoal)}
.btn-contact{top:913px;left:461px;width:263px;height:48px;border:3px solid var(--coral);color:var(--coral)}

/* services */
.services{top:1050px;left:0;width:1200px;height:789px;background:var(--peach)}
.service-icon{position:absolute;top:1287px;width:174px;height:174px}
.service-name{position:absolute;font-family:"Lato",sans-serif;font-size:30px;line-height:36px;color:var(--charcoal)}
.service-desc{position:absolute;top:1580px;font-size:13px;line-height:16px;font-weight:700;color:var(--muted)}
.btn-learn{top:1638px;width:178px;height:32px;border:3px solid var(--coral);color:var(--coral);font-size:14px;border-radius:7px}

/* projects */
.projects-text{top:2066px;left:215px;width:800px;font-size:22px;line-height:30px;color:var(--charcoal)}
.shot{position:absolute;border:2px solid #9a9a9a}
.shot-blue{background:linear-gradient(180deg,#2f4a6a 0%,#8da6bf 55%,#f2f2f2 100%)}
.shot-sky{background:linear-gradient(180deg,#f4f4f4 0%,#9fb6c9 30%,#6f7f8a 70%,#e9ecef 100%)}
.shot-kitchen{background:linear-gradient(180deg,#3b4450 0%,#4d5763 55%,#f4f4f4 100%)}
.shot-green{background:linear-gradient(180deg,#2a2a2a 0%,#6a6f66 50%,#ececec 100%)}
.shot-light{background:linear-gradient(180deg,#f3f3f3 0%,#d9d9d9 100%)}
.shot-ambulance{background:linear-gradient(180deg,#e6edf5 0%,#2d5e9c 45%,#e8c84a 100%)}
.shot-people{background:linear-gradient(180deg,#f3f3f3 0%,#4f7fc4 40%,#c9a46e 100%)}
.btn-more{top:2943px;left:467px;width:264px;height:48px;border:3px solid var(--violet);color:var(--violet)}

/* who we are */
.who{top:3061px;left:0;width:1200px;height:1297px;background:var(--green)}
.who .section-title{color:var(--charcoal)}
.who-text{top:3296px;left:176px;width:850px;font-size:19px;line-height:30px;color:var(--green-text)}
.btn-quote{top:3532px;left:467px;width:264px;height:48px;border:3px solid var(--white);color:var(--white);font-weight:700}
.testimonial{position:absolute;top:3806px;width:259px;height:370px;background:var(--card);box-shadow:0 4px 10px rgba(0,0,0,.25);padding:0 18px}
.avatar{position:absolute;top:24px;left:89px;width:82px;height:82px;border-radius:50%;border:3px solid var(--white)}
.quote{position:absolute;top:130px;left:18px;width:225px;font-size:11px;line-height:13px;color:var(--muted)}
.reviewer{position:absolute;top:268px;left:18px;width:225px;font-size:11px;line-height:13px;color:var(--muted)}
.reviewer strong{font-weight:700}
.dot{position:absolute;top:4279px;width:18px;height:18px;border-radius:50%;border:2px solid #111}

/* footer */
.footer{top:4358px;left:0;width:1200px;height:394px;background:var(--charcoal)}
.footer-line{position:absolute;font-size:14px;line-height:16px;color:var(--white)}
.newsletter-title{top:4515px;left:761px;font-weight:700;font-size:14px;color:var(--white)}
.newsletter{position:absolute;top:4541px;left:763px;width:260px;height:42px;border:2px solid var(--white);display:flex}
.newsletter .field{flex:1;font-size:13px;color:var(--white);padding:11px 14px}
.newsletter .submit{width:80px;border-left:2px solid var(--white);font-size:13px;font-weight:700;color:var(--white);display:flex;align-items:center;justify-content:center}
.bottom-bar{top:4752px;left:0;width:1200px;height:21px;background:var(--coral);font-size:12px;color:var(--white);text-align:center;line-height:21px}
</style>
</head>
<body>

<div class="abs top-bar">
  <span class="social-dot" style="left:738px"></span>
  <span class="social-dot" style="left:801px"></span>
  <span class="social-dot" style="left:866px"></span>
  <span class="social-dot" style="left:930px"></span>
  <span class="social-dot" style="left:993px"></span>
</div>

<header class="abs hero" role="img" aria-label="Photo of a desk with a code-filled monitor, a keyboard and an iced coffee"></header>
<div class="brand" style="top:106px;left:174px">Rise And Reach</div>
<nav class="nav"><span>WHAT WE DO</span><span>PROJECTS</span><span>WHO WE ARE</span><span>BOOK US</span></nav>
<p class="hero-text">Rise And Reach is a leading Easton web design and inbound marketing agency focused on client results.</p>

<p class="abs intro-text">We offer responsive web design services, search engine marketing, social media marketing, content creation and more.</p>
<div class="btn btn-contact">Contact Us</div>

<section class="abs services"></section>
<h2 class="section-title" style="top:1124px">OUR SERVICES</h2>
<div class="title-rule" style="top:1206px"></div>

<svg class="service-icon" style="left:215px" viewBox="0 0 174 174" aria-hidden="true">
  <circle cx="87" cy="87" r="84" fill="none" stroke="var(--ink)" stroke-width="4"/>
  <rect x="42" y="45" width="90" height="66" rx="4" fill="none" stroke="var(--ink)" stroke-width="4"/>
  <rect x="52" y="55" width="70" height="46" fill="none" stroke="var(--coral)" stroke-width="3"/>
  <line x1="60" y1="68" x2="84" y2="68" stroke="var(--coral)" stroke-width="3"/>
  <line x1="92" y1="68" x2="114" y2="68" stroke="var(--coral)" stroke-width="3"/>
  <line x1="92" y1="78" x2="114" y2="78" stroke="var(--coral)" stroke-width="3"/>
  <line x1="92" y1="88" x2="114" y2="88" stroke="var(--coral)" stroke-width="3"/>
  <path d="M77 111 L72 128 H102 L97 111" fill="none" stroke="var(--ink)" stroke-width="4"/>
</svg>
<svg class="service-icon" style="left:511px" viewBox="0 0 174 174" aria-hidden="true">
  <circle cx="87" cy="87" r="84" fill="none" stroke="var(--ink)" stroke-width="4"/>
  <rect x="46" y="104" width="16" height="26" fill="none" stroke="var(--coral)" stroke-width="4"/>
  <rect x="72" y="86" width="16" height="44" fill="none" stroke="var(--coral)" stroke-width="4"/>
  <rect x="98" y="94" width="16" height="36" fill="none" stroke="var(--coral)" stroke-width="4"/>
  <rect x="124" y="66" width="16" height="64" fill="none" stroke="var(--coral)" stroke-width="4"/>
  <path d="M44 88 L70 64 L92 76 L132 36" fill="none" stroke="var(--coral)" stroke-width="4"/>
  <path d="M116 36 H132 V52" fill="none" stroke="var(--coral)" stroke-width="4"/>
  <line x1="38" y1="132" x2="146" y2="132" stroke="var(--ink)" stroke-width="4"/>
</svg>
<svg class="service-icon" style="left:808px" viewBox="0 0 174 174" aria-hidden="true">
  <circle cx="87" cy="87" r="84" fill="none" stroke="var(--ink)" stroke-width="4"/>
  <circle cx="56" cy="88" r="22" fill="none" stroke="var(--ink)" stroke-width="4"/>
  <circle cx="56" cy="82" r="7" fill="none" stroke="var(--ink)" stroke-width="3"/>
  <path d="M44 102 Q56 88 68 102" fill="none" stroke="var(--ink)" stroke-width="3"/>
  <circle cx="118" cy="56" r="20" fill="none" stroke="var(--coral)" stroke-width="4"/>
  <circle cx="118" cy="51" r="6" fill="none" stroke="var(--coral)" stroke-width="3"/>
  <path d="M107 69 Q118 56 129 69" fill="none" stroke="var(--coral)" stroke-width="3"/>
  <circle cx="118" cy="120" r="20" fill="none" stroke="var(--coral)" stroke-width="4"/>
  <circle cx="118" cy="115" r="6" fill="none" stroke="var(--coral)" stroke-width="3"/>
  <path d="M107 133 Q118 120 129 133" fill="none" stroke="var(--coral)" stroke-width="3"/>
  <line x1="77" y1="80" x2="99" y2="64" stroke="var(--coral)" stroke-width="3"/>
  <line x1="77" y1="96" x2="99" y2="112" stroke="var(--coral)" stroke-width="3"/>
</svg>

<h3 class="service-name" style="top:1488px;left:212px">Web Design</h3>
<h3 class="service-name" style="top:1492px;left:559px">S.E.O.</h3>
<h3 class="service-name" style="top:1486px;left:794px">Social Media<br>Management</h3>
<p class="service-desc" style="left:178px;width:260px">Turn website visitors into customers with engaging content and compelling design.</p>
<p class="service-desc" style="left:465px;width:270px">Search engine optimization for more traffic.</p>
<p class="service-desc" style="left:792px;width:230px">Manage your online presence on social media platforms.</p>
<div class="btn btn-learn" style="left:206px">Learn more</div>
<div class="btn btn-learn" style="left:508px">Learn more</div>
<div class="btn btn-learn" style="left:802px">Learn more</div>

<h2 class="section-title" style="top:1907px">PROJECTS</h2>
<div class="title-rule" style="top:1992px"></div>
<p class="abs projects-text">All our custom websites are built with responsive design so they will look great on desktops, tablets, and mobile phones.</p>

<div class="shot shot-blue" style="left:174px;top:2195px;width:415px;height:307px" role="img" aria-label="Homebuilder website shown on desktop and phone"></div>
<div class="shot shot-sky" style="left:611px;top:2195px;width:417px;height:307px" role="img" aria-label="Roofing company website shown on desktop and phone"></div>
<div class="shot shot-green" style="left:174px;top:2563px;width:197px;height:147px" role="img" aria-label="Junk removal company website"></div>
<div class="shot shot-light" style="left:394px;top:2563px;width:197px;height:147px" role="img" aria-label="Service business website on desktop and phone"></div>
<div class="shot shot-ambulance" style="left:174px;top:2726px;width:197px;height:147px" role="img" aria-label="Ambulance billing website"></div>
<div class="shot shot-people" style="left:394px;top:2726px;width:197px;height:147px" role="img" aria-label="Community organisation website"></div>
<div class="shot shot-kitchen" style="left:611px;top:2563px;width:417px;height:310px" role="img" aria-label="Kitchen and bath remodeler website shown on desktop and phone"></div>
<div class="btn btn-more">See more</div>

<section class="abs who" role="img" aria-label="Green band with faint palm leaf pattern"></section>
<h2 class="section-title" style="top:3139px">WHO WE ARE</h2>
<div class="title-rule" style="top:3222px"></div>
<p class="abs who-text">We're the most reviewed and highest rated Web Design company in Easton that focuses on services that include inbound marketing, search engine optimization, social media marketing, lead conversion, to nurturing, and marketing automation. We perform high-end mobile-friendly web design, content creation, SEO, social media strategy development, email marketing, and more. Our clients in Easton and around the country enjoy more website visitors, more conversions, and best of all a better return on investment.</p>
<div class="btn btn-quote">Request Quote</div>

<h2 class="section-title" style="top:3683px">TESTIMONIALS</h2>

<article class="testimonial" style="left:172px">
  <div class="avatar" style="background:linear-gradient(135deg,#e58a5a,#c9c3bd)" role="img" aria-label="Portrait of Mira Halvorsen"></div>
  <p class="quote">“Mira and her team were incredibly responsive, resourceful, and diligent. Dean specifically translated “non-web savvy” ideas promoted by us, into a site that exceeded our expectations. We would recommend Rise And Reach to anyone considering anything to do with website design, SEO, and marketing!”</p>
  <p class="reviewer"><strong>Mira Halvorsen</strong><br>Managing Member, Northgate Equity Group</p>
</article>
<article class="testimonial" style="left:472px">
  <div class="avatar" style="background:linear-gradient(135deg,#d9d9d9,#8a8a8a)" role="img" aria-label="Portrait of Dean Whitlock"></div>
  <p class="quote">“Dean Whitlock at Rise and Reach has been terrific to work with. Dean provided valuable direction and insight. If you are looking for creative talent and strategic direction, Rise And Reach is a good place to start.”</p>
  <p class="reviewer"><strong>Dean Whitlock</strong><br>Founder &amp; CEO, Clearview Care Services</p>
</article>
<article class="testimonial" style="left:769px">
  <div class="avatar" style="background:linear-gradient(135deg,#cfc7bd,#6d5a48)" role="img" aria-label="Portrait of Leo Marchetti"></div>
  <p class="quote">“Rise and Reach just redesigned our nonprofit website and we couldn't be happier with the results. The team is very pleasing to work with, professional, responsive to our requests and always made sure that the product met our expectations. I would definitely recommend Rise And Reach to anyone looking to create or redesign their website!”</p>
  <p class="reviewer"><strong>Leo Marchetti</strong><br>Secretary &amp; Chief Operational Officer, Island Relief Network</p>
</article>

<svg class="abs" style="top:4208px;left:560px" width="80" height="46" viewBox="0 0 80 46" aria-hidden="true">
  <path d="M30 4 L10 23 L30 42" fill="none" stroke="#111" stroke-width="6"/>
  <path d="M50 4 L70 23 L50 42" fill="none" stroke="#111" stroke-width="6"/>
</svg>
<span class="dot" style="left:544px;background:#111"></span>
<span class="dot" style="left:572px"></span>
<span class="dot" style="left:600px"></span>
<span class="dot" style="left:628px"></span>

<footer class="abs footer"></footer>
<div class="brand" style="top:4402px;left:174px">Rise And Reach</div>

<svg class="abs" style="top:4518px;left:174px" width="20" height="20" viewBox="0 0 20 20" aria-hidden="true"><path d="M4 2 L8 2 L9 6 L7 8 Q9 12 12 13 L14 11 L18 12 L18 16 Q17 18 15 18 Q3 16 2 4 Q2 2 4 2Z" fill="none" stroke="var(--white)" stroke-width="1.5"/></svg>
<p class="footer-line" style="top:4521px;left:202px">555-014-2290</p>

<svg class="abs" style="top:4577px;left:174px" width="20" height="16" viewBox="0 0 20 16" aria-hidden="true"><rect x="1" y="1" width="18" height="14" fill="none" stroke="var(--white)" stroke-width="1.5"/><path d="M1 1 L10 9 L19 1" fill="none" stroke="var(--white)" stroke-width="1.5"/></svg>
<p class="footer-line" style="top:4578px;left:202px">HELLO@RISEANDREACH.EXAMPLE</p>

<svg class="abs" style="top:4628px;left:174px" width="22" height="22" viewBox="0 0 22 22" aria-hidden="true"><circle cx="11" cy="11" r="9.5" fill="none" stroke="var(--white)" stroke-width="1.5"/><path d="M11 5 V11 L15 13" fill="none" stroke="var(--white)" stroke-width="1.5"/></svg>
<p class="footer-line" style="top:4626px;left:202px">OPERATING HOURS:<br>Mon-Sat, 8AM – 8PM</p>

<svg class="abs" style="top:4516px;left:522px" width="16" height="22" viewBox="0 0 16 22" aria-hidden="true"><path d="M8 21 Q1 12 1 8 A7 7 0 0 1 15 8 Q15 12 8 21Z" fill="none" stroke="var(--white)" stroke-width="1.5"/><circle cx="8" cy="8" r="2.5" fill="none" stroke="var(--white)" stroke-width="1.5"/></svg>
<p class="footer-line" style="top:4514px;left:548px">Harborline Web Studio<br>88 Pier Lane #210<br>Easton, MA 02375<br>555-014-2290</p>

<p class="abs newsletter-title">Get News, Events &amp; Freebies</p>
<div class="newsletter"><span class="field">Your e-mail</span><span class="submit">Sign Up</span></div>

<div class="abs bottom-bar">©2021 RISE AND REACH</div>

</body>
</html>
```